Textbook cover for educational dental hygiene seminar

A professional and trendy textbook cover design to be used. 8.5 x 11 with full bleed, cmyk, and a count for binding when designed. Year 2023 displayed, and title BelvaKTO’s Dental Hygiene Academy. Colors- shades of purple, white, and black. Please also use logo. Website www.BelvaKTOPrepCourse.example

For background- maybe ombré, or some sort of trendy design. Display a big tooth on the front.

Colors
6B429C
8869AF
B7A5CE
E3DAEB
F3F0F8

```html
<!DOCTYPE html>
<html lang="en">
<head>
<meta charset="utf-8">
<title>BelvaKTO’s Dental Hygiene Academy 2023 – Cover</title>
<link href="https://fonts.googleapis.com/css2?family=DM+Serif+Display&family=Montserrat:wght@500;700&display=swap" rel="stylesheet">
<style>
  :root {
    --page-bg: #d3d3d3;
    --cover-deep: #12056a;
    --cover-mid: #1c0880;
    --cover-glow: #5b12c9;
    --tooth-purple: #7b3c9c;
    --tooth-soft: #8869af;
    --text-white: #ffffff;
    --rule-white: #e3daeb;
  }
  * { margin: 0; padding: 0; box-sizing: border-box; }
  html, body {
    width: 750px; height: 1200px; overflow: hidden;
    background: var(--page-bg);
  }
  .cover {
    position: absolute;
    left: 25px; top: 147px;
    width: 700px; height: 906px;
    background:
      radial-gradient(ellipse 260px 300px at 68% 42%, var(--cover-glow) 0%, rgba(91,18,201,0) 100%),
      linear-gradient(160deg, var(--cover-deep) 0%, var(--cover-mid) 55%, var(--cover-deep) 100%);
    color: var(--text-white);
    text-align: center;
    overflow: hidden;
  }
  .cover-title {
    position: absolute; top: 58px; left: 0; right: 0;
    font-family: "DM Serif Display", serif;
    font-weight: 400;
    font-size: 76px; line-height: 1;
    letter-spacing: -1px;
  }
  .cover-subtitle {
    position: absolute; top: 146px; left: 0; right: 0;
    font-family: "Montserrat", sans-serif;
    font-weight: 500;
    font-size: 30px; letter-spacing: 1.5px;
  }
  .cover-year {
    position: absolute; top: 186px; left: 118px; right: 118px;
    display: flex; align-items: center; gap: 16px;
  }
  .cover-year .rule { flex: 1; height: 1.5px; background: var(--rule-white); }
  .cover-year .year {
    font-family: "DM Serif Display", serif;
    font-size: 68px; line-height: 1;
  }
  .tooth-art {
    position: absolute; left: 150px; top: 280px;
    width: 400px; height: 480px;
    border-radius: 48% 48% 40% 40% / 42% 42% 58% 58%;
    background: radial-gradient(ellipse at 50% 45%, rgba(136,105,175,0.55) 0%, rgba(123,60,156,0.35) 55%, rgba(123,60,156,0) 100%);
  }
  .academy-mark {
    position: absolute; left: 200px; top: 365px;
    width: 300px; height: 300px;
    display: flex; flex-direction: column; align-items: center; justify-content: center;
    gap: 14px;
  }
  .academy-mark .dot {
    width: 70px; height: 70px; border-radius: 50%;
    background: var(--text-white);
  }
  .academy-mark .name {
    font-family: "Montserrat", sans-serif;
    font-weight: 700; font-size: 20px; line-height: 1.3;
    color: var(--text-white);
  }
  .cover-tagline {
    position: absolute; top: 820px; left: 0; right: 0;
    font-family: "Montserrat", sans-serif;
    font-weight: 700; font-size: 21px;
  }
  .cover-url {
    position: absolute; top: 852px; left: 0; right: 0;
    font-family: "Montserrat", sans-serif;
    font-weight: 500; font-size: 19px; letter-spacing: 0.5px;
  }
  .cover-url b { font-weight: 700; }
</style>
</head>
<body>
  <main class="cover">
    <h1 class="cover-title">BELVAKTO’S</h1>
    <p class="cover-subtitle">DENTAL HYGIENE ACADEMY</p>
    <div class="cover-year"><span class="rule"></span><span class="year">2023</span><span class="rule"></span></div>
    <div class="tooth-art" role="img" aria-label="Large purple outlined tooth illustration"></div>
    <div class="academy-mark">
      <span class="dot"></span>
      <span class="name">BelvaKTO’s<br>Dental Hygiene Academy</span>
    </div>
    <p class="cover-tagline">The World’s First Interactive Review Book!</p>
    <p class="cover-url">www.<b>BelvaKTOPrepCourse</b>.example</p>
  </main>
</body>
</html>
```